we need a new logo and business card and package label for my cake business.
looking for a fresh and standout design.

i have attached my old card to this.

Industry/Entity Type

Hospitality

Contact Information for Business Card

Marisol Penhallow
email: marip58@quillpost.example
facebook:www.facebook.com/sollyovenworks
mobile:0481236907

Logo Text

Desserts By Solly P

Font styles to use
Decorative

Colors
ed2930
f04a51
b768aa
0356a4
33a6d7

Requirements
Must have
• standout design
• grab attention

```html
<!DOCTYPE html>
<html lang="en">
<head>
<meta charset="utf-8">
<title>Desserts By Solly P — Business Card</title>
<link rel="stylesheet" href="https://fonts.googleapis.com/css2?family=Lato:wght@400;700;900&display=swap">
<style>
  :root {
    --coral: #f04a51;
    --red: #ed2930;
    --plum: #b768aa;
    --ink: #333333;
    --paper: #ffffff;
    --backdrop: #ecebe8;
  }
  * { box-sizing: border-box; margin: 0; padding: 0; }
  html, body { width: 1200px; height: 900px; overflow: hidden; }
  body {
    background: var(--backdrop);
    font-family: "Lato", Arial, sans-serif;
    position: relative;
  }
  .card {
    position: absolute;
    width: 520px;
    height: 297px;
    border-radius: 4px;
    overflow: hidden;
    box-shadow: 0 6px 18px rgba(0,0,0,0.18);
  }
  /* Front */
  .card-front {
    left: 50px; top: 302px;
    background: var(--coral);
    display: flex;
    flex-direction: column;
    align-items: center;
    justify-content: center;
    gap: 18px;
  }
  .front-mark {
    width: 118px; height: 118px;
    border: 5px solid var(--paper);
    border-radius: 50%;
  }
  .front-name {
    color: var(--paper);
    font-weight: 900;
    font-size: 34px;
    letter-spacing: 0.3px;
  }
  /* Back */
  .card-back {
    left: 630px; top: 302px;
    background: var(--paper);
  }
  .back-wave { position: absolute; inset: 0; }
  .holder {
    position: absolute; left: 30px; top: 42px;
  }
  .holder-name {
    font-size: 21px;
    font-weight: 700;
    letter-spacing: 0.5px;
    text-transform: uppercase;
  }
  .holder-first { color: var(--coral); }
  .holder-last { color: var(--plum); }
  .holder-role {
    font-size: 14px;
    color: var(--ink);
    margin-top: 2px;
  }
  .brand {
    position: absolute; right: 26px; top: 28px;
    width: 200px;
    display: flex; flex-direction: column; align-items: center; gap: 10px;
  }
  .brand-mark {
    width: 78px; height: 78px;
    border: 4px solid var(--plum);
    border-radius: 50%;
  }
  .brand-name {
    color: var(--coral);
    font-weight: 700;
    font-size: 21px;
    white-space: nowrap;
  }
  .contacts {
    position: absolute; left: 30px; top: 166px;
    list-style: none;
    display: flex; flex-direction: column; gap: 4px;
  }
  .contact {
    display: flex; align-items: center; gap: 7px;
    font-size: 14px; color: var(--ink);
  }
  .contact-icon {
    width: 16px; height: 16px; flex: none;
    border-radius: 50%;
    background: var(--coral);
    display: flex; align-items: center; justify-content: center;
  }
</style>
</head>
<body>
  <section class="card card-front" aria-label="Business card front">
    <div class="front-mark" aria-hidden="true"></div>
    <div class="front-name">Desserts By Solly P</div>
  </section>

  <section class="card card-back" aria-label="Business card back">
    <svg class="back-wave" viewBox="0 0 520 297" preserveAspectRatio="none" aria-hidden="true">
      <path d="M0 244 C170 250 320 214 430 160 C340 226 170 262 0 262 Z" fill="var(--plum)"/>
      <path d="M0 262 C170 262 330 226 430 160 C470 140 500 130 520 124 L520 297 L0 297 Z" fill="var(--coral)"/>
    </svg>

    <div class="holder">
      <div class="holder-name"><span class="holder-first">Marisol</span> <span class="holder-last">Penhallow</span></div>
      <div class="holder-role">Qualified Chef and Pastry Chef</div>
    </div>

    <div class="brand">
      <div class="brand-mark" aria-hidden="true"></div>
      <div class="brand-name">Desserts By Solly P</div>
    </div>

    <ul class="contacts">
      <li class="contact">
        <span class="contact-icon" aria-hidden="true">
          <svg width="10" height="10" viewBox="0 0 10 10"><path d="M2 1 L4 1 L4.6 3 L3.5 3.8 C4 5 5 6 6.2 6.5 L7 5.4 L9 6 L9 8 C9 8.6 8.5 9 8 9 C4 9 1 6 1 2 C1 1.5 1.4 1 2 1 Z" fill="#fff"/></svg>
        </span>
        0481236907
      </li>
      <li class="contact">
        <span class="contact-icon" aria-hidden="true">
          <svg width="10" height="10" viewBox="0 0 10 10"><rect x="1" y="2.2" width="8" height="5.6" fill="none" stroke="#fff" stroke-width="1"/><path d="M1 2.4 L5 5.4 L9 2.4" fill="none" stroke="#fff" stroke-width="1"/></svg>
        </span>
        marip58@quillpost.example
      </li>
      <li class="contact">
        <span class="contact-icon" aria-hidden="true"></span>
        /sollyovenworks
      </li>
    </ul>
  </section>
</body>
</html>
```